Präsentationsvorlagen
Zielgruppe
Die velora systems GmbH ist ein kleines Beratungsunternehmen mit drei Beratern, das sich auf Brightwell 365-Beratung spezialisiert hat. Das Unternehmen bietet Dienstleistungen in den Bereichen Security, Compliance und Device Management an, insbesondere mit Brightwell Keystra.
Darüber hinaus entwickelt velora systems das SaaS-Produkt 'Tandemo', das überprüft, ob ein B365-Tenant sicher konfiguriert ist. Tandemo basiert auf eigenen Best Practices und wird durch ein Rechtsgutachten ergänzt, um die Sicherheit eines Tenants auch aus juristischer Sicht zu bewerten.
Zielgruppe von velora systems
IT-Leiter und IT-Administratoren, die für Brightwell 365 und Security verantwortlich sind
Unternehmen, die Brightwell Keystra für ihre Geräteverwaltung einsetzen oder dies planen
IT-Dienstleister, die Security- und Compliance-Anforderungen für ihre Kunden umsetzen müssen
Krankenkassen und andere regulierte Branchen, die eine sichere und gesetzeskonforme B365-Umgebung benötigen
Aufgabenstellung
1. General Design & Functional Principles
1.1 Corporate Identity (CI) Integration
All templates must use the company’s branding (colors, fonts, logos, spacing).
Ensure that SmartArt, shapes, tables, and lists automatically adopt the branded theme when newly created.
1.2 Print & PDF Export Compatibility
Templates must translate well into A4-sized PDFs and remain visually consistent in print.
Avoid distortions when exporting or printing.
1.3 Accessibility & Readability
Maintain high contrast and readable font sizes.
Alternative text must be included for all images and media.
Support for screen readers and keyboard navigation must be ensured across all templates.
1.4 AI & Pathmate Optimization
Placeholders should include AI-friendly prompts, such as:
'Summarize this section in one sentence.'
'List three key takeaways from this slide.'
'Rewrite this paragraph at a C-suite level.'
'Generate an executive summary.'
'Provide a bulleted version of this paragraph.'
Naming conventions for placeholders should follow a structured format for AI reference, e.g.:
Executive_Summary_Box
Decision_Options_Table
Key_Takeaways_List
1.5 Flexible Content Accommodation
List-based content must support short and long variants (e.g., 3-5 items, 6-10 items).
1.6 Default Theme for Newly Created Elements
Ensure that default tables, charts, SmartArt, and shapes adopt the corporate theme.
Layouts:
Title Slide (Introduction & Branding)
Sets the stage for the presentation by introducing the topic, presenter, and company.
Includes: Main title, subtitle, company logo, and optional background image.
Agenda Slide (Navigation & Structure)
Provides an overview of the key topics and sections to help the audience follow along.
Includes: A clear agenda list (short or extended), optional icons for visual appeal.
Section Header Slide (Transitions & ..

```html
<!DOCTYPE html>
<html lang="de">
<head>
<meta charset="utf-8">
<title>velora systems – Präsentationsvorlagen</title>
<link rel="stylesheet" href="https://fonts.googleapis.com/css2?family=Barlow:wght@400;500;600;700&display=swap">
<style>
:root{
  --canvas:#e4e4e4;
  --olive:#c0bc06;
  --olive-soft:#d4d246;
  --bright:#d8d700;
  --slate:#5e666b;
  --mist:#9ea7ad;
  --grid:#d5d8da;
  --white:#ffffff;
  --ink:#1e1e1e;
}
*{box-sizing:border-box;margin:0;padding:0}
html,body{width:1200px;height:2395px;overflow:hidden}
body{background:var(--canvas);font-family:"Barlow",sans-serif;color:var(--ink)}
.deck{position:absolute;left:25px;top:29px;display:grid;grid-template-columns:549px 549px;column-gap:55px;row-gap:27px}
.slide{position:relative;width:549px;height:309px;overflow:hidden}
.bg-olive{background:var(--olive)}
.bg-white{background:var(--white)}
.abs{position:absolute}

.logo{position:absolute;left:417px;top:30px;display:flex;align-items:center;gap:6px;font-weight:600;font-size:11px;letter-spacing:.08em;text-transform:uppercase;white-space:nowrap}
.logo .mark{width:14px;height:14px}
.logo.on-olive{color:var(--white)}
.logo.on-olive .mark{background:var(--white)}
.logo.on-white{color:var(--slate)}
.logo.on-white .mark{background:var(--slate)}

.footer{position:absolute;left:31px;top:274px;font-size:6.5px;color:var(--slate)}
.bg-olive .footer{color:var(--white)}
.page{position:absolute;right:0;top:268px;width:31px;height:18px;background:var(--slate);color:var(--white);font-size:6px;display:flex;align-items:center;justify-content:center}
.page.light{background:var(--white);color:var(--slate)}

.headline{position:absolute;font-weight:500;font-size:25px;line-height:1.05;color:var(--slate)}
.rule{position:absolute;height:1.5px;background:var(--slate)}
.lead{position:absolute;font-size:6.8px;line-height:1.35;color:#333}

.hero-title{position:absolute;left:42px;font-weight:600;font-size:30px;color:var(--white);padding-left:14px;border-left:none}
.hero-title::before{content:"";position:absolute;left:0;top:6px;width:2.5px;height:24px;background:var(--slate)}
.caption-band{position:absolute;text-align:center}
.caption-band span{display:table;margin:0 auto;background:var(--slate);color:var(--white);font-size:11.5px;line-height:17px;padding:0 11px}

.agenda-label{position:absolute;left:259px;font-size:7.5px;font-weight:600;color:var(--slate);letter-spacing:.04em}
.agenda-bar{position:absolute;left:307px;width:171px;height:18px;background:var(--olive);color:var(--white);font-size:8.5px;padding-left:18px;line-height:18px}

.list-box{position:absolute;background:var(--olive);color:#f3f2c6;font-size:8.5px;line-height:11.4px;padding:17px 0 0 20px}
.list-box ul,.list-box ol,.panel-list ul,.panel-list ol{list-style:none}

.panel{position:absolute;left:396px;top:0;width:135px;height:309px;background:var(--slate)}
.panel-list{position:absolute;color:#e8ebec;font-size:8.5px;line-height:11.4px}

.stat{position:absolute;color:var(--white);text-align:center;display:flex;flex-direction:column;justify-content:center;align-items:center}
.stat b{font-weight:600;line-height:1}
.stat small{display:block;font-size:7px;line-height:1.2}
.stat.olive{background:var(--olive)}
.stat.slate{background:var(--slate)}
.stat.mist{background:var(--mist)}
.stat.bright{background:var(--bright)}
.stat.mini small{font-size:4.5px;margin-top:2px}

.chart{position:absolute;left:0;top:0}
.chart text{font-family:"Barlow",sans-serif}

.table-head{position:absolute;top:80px;width:71px;text-align:center;color:var(--white);font-weight:600;font-size:10px}

.compare{position:absolute;top:171px;width:246px;height:70px;background:var(--olive);display:flex}
.compare .swatch{width:70px;background:var(--bright)}
.compare .body{padding:11px 0 0 18px;color:var(--white);font-size:7.5px;line-height:11px}
.compare .body strong{font-weight:600}
.compare ul{list-style:none;padding-left:8px}

.tl-dot{position:absolute;width:30px;height:30px;border-radius:50%;background:var(--bright)}
.tl-label{position:absolute;font-size:6.5px;color:var(--olive);width:80px;text-align:center}
.tl-date{position:absolute;top:246px;font-size:6.5px;color:var(--slate)}

.step-head{position:absolute;width:153px;height:16px;background:var(--olive-soft);color:var(--white);font-size:7.5px;line-height:16px;padding-left:9px;font-weight:500}
.step-box{position:absolute;width:153px;height:52px;background:var(--slate);color:var(--white);font-size:8px;line-height:10.5px;padding:11px 9px 0}

.close-step{position:absolute;left:223px;font-size:7.5px;font-weight:600;color:var(--olive)}
.close-text{position:absolute;left:311px;font-size:7px;color:var(--slate)}
.close-rule{position:absolute;left:223px;width:232px;height:.8px;background:#cfd3d5}

.contact-line{position:absolute;left:372px;font-size:8.5px;color:var(--slate);line-height:11px}
</style>
</head>
<body>
<main class="deck">

  <!-- Title slide -->
  <section class="slide bg-olive">
    <div class="logo on-olive"><span class="mark"></span>velora systems</div>
    <h1 class="hero-title" style="top:88px">Title Slide</h1>
    <div class="caption-band" style="left:150px;top:171px;width:266px">
      <span>Sets the stage for the presentation by introducing</span>
      <span>the topic, presenter, and company.</span>
    </div>
    <p class="footer">Presented By Presenter | velora systems</p>
  </section>

  <!-- Agenda slide -->
  <section class="slide bg-white">
    <div class="logo on-white"><span class="mark"></span>velora systems</div>
    <h2 class="headline" style="left:31px;top:42px">Agenda<br>Slide</h2>
    <div class="rule" style="left:31px;top:103px;width:153px"></div>
    <span class="agenda-label" style="top:108px">PART 1</span><div class="agenda-bar" style="top:101px">Key Topic 01</div>
    <span class="agenda-label" style="top:137px">PART 2</span><div class="agenda-bar" style="top:130px">Key Topic 02</div>
    <span class="agenda-label" style="top:166px">PART 3</span><div class="agenda-bar" style="top:159px">Key Topic 03</div>
    <span class="agenda-label" style="top:195px">PART 4</span><div class="agenda-bar" style="top:188px">Key Topic 04</div>
    <span class="agenda-label" style="top:224px">PART 5</span><div class="agenda-bar" style="top:218px">Key Topic 05</div>
    <p class="footer">Presented By Presenter | velora systems</p>
  </section>

  <!-- Section header slide -->
  <section class="slide">
    <div class="abs" role="img" aria-label="Hintergrundfoto: Person am Laptop am Schreibtisch, olivgrün eingefärbt" style="inset:0;background:linear-gradient(120deg,#b9b51a 0%,#c9c63c 45%,#d8d66e 100%)"></div>
    <div class="logo on-olive"><span class="mark"></span>velora systems</div>
    <h1 class="hero-title" style="top:124px">Section Header Slide</h1>
    <div class="caption-band" style="left:234px;top:218px;width:276px">
      <span>Clearly marks new sections in the presentation,</span>
      <span>making content transitions smoother.</span>
    </div>
  </section>

  <!-- Content slide, white -->
  <section class="slide bg-white">
    <div class="logo on-white"><span class="mark"></span>velora systems</div>
    <h2 class="headline" style="left:30px;top:56px">Content Slide</h2>
    <div class="rule" style="left:30px;top:85px;width:144px"></div>
    <p class="lead" style="left:30px;top:99px;width:190px">Presents structured textual information in a way that is easy to read and digest. Includes: Headings, paragraphs, bullet points, numbered lists, optional icons for clarity.</p>
    <div class="list-box" style="left:234px;top:143px;width:133px;height:88px">
      <ul><li>• Point 01</li><li>• Point 02</li><li>• Point 03</li><li>• Point 04</li><li>• Point 05</li></ul>
    </div>
    <div class="list-box" style="left:389px;top:143px;width:132px;height:88px">
      <ol><li>1.&nbsp; Number 01</li><li>2.&nbsp; Number 02</li><li>3.&nbsp; Number 03</li><li>4.&nbsp; Number 04</li><li>5.&nbsp; Number 05</li></ol>
    </div>
    <p class="footer">Presented By Presenter | velora systems</p>
    <div class="page">4</div>
  </section>

  <!-- Content slide, olive with panel -->
  <section class="slide bg-olive">
    <div class="panel"></div>
    <div class="logo on-olive"><span class="mark"></span>velora systems</div>
    <h2 class="headline" style="right:208px;top:112px">Content Slide</h2>
    <p class="lead" style="right:208px;top:157px;width:190px;text-align:right;color:var(--slate)">Presents structured textual information in a way that is easy to read and digest. Includes: Headings, paragraphs, bullet points, numbered lists, optional icons for clarity.</p>
    <div class="panel-list" style="left:419px;top:84px"><ul><li>• Point 01</li><li>• Point 02</li><li>• Point 03</li><li>• Point 04</li><li>• Point 05</li></ul></div>
    <div class="panel-list" style="left:421px;top:172px"><ol><li>1.&nbsp; Number 01</li><li>2.&nbsp; Number 02</li><li>3.&nbsp; Number 03</li><li>4.&nbsp; Number 04</li><li>5.&nbsp; Number 05</li></ol></div>
    <div class="page light" style="right:0">5</div>
  </section>

  <!-- Line slide -->
  <section class="slide bg-white">
    <h2 class="headline" style="left:31px;top:41px">Line Slide</h2>
    <div class="rule" style="left:31px;top:70px;width:145px"></div>
    <p class="lead" style="left:31px;top:84px;width:180px">Helps communicate data-driven insights in a visually compelling manner. Includes: Bar charts, pie charts, line graphs, and consistent formatting for clarity.</p>
    <div class="stat olive" style="left:267px;top:39px;width:92px;height:69px"><b style="font-size:27px">100</b><small>readers appreciate<br>accurate information</small></div>
    <div class="stat slate" style="left:376px;top:39px;width:92px;height:69px"><b style="font-size:27px">75</b><small>readers appreciate<br>accurate information</small></div>
    <svg class="chart" width="549" height="309" viewBox="0 0 549 309" role="img" aria-label="Liniendiagramm mit zwei Datenreihen über Data 01 bis Data 04">
      <g stroke="var(--grid)" stroke-width=".8">
        <line x1="47" y1="138" x2="507" y2="138"/><line x1="47" y1="165" x2="507" y2="165"/>
        <line x1="47" y1="192" x2="507" y2="192"/><line x1="47" y1="219" x2="507" y2="219"/>
      </g>
      <g font-size="6.5" fill="var(--ink)">
        <text x="31" y="140">100</text><text x="34" y="167">75</text><text x="34" y="194">50</text><text x="34" y="221">25</text><text x="38" y="248">0</text>
        <text x="37" y="257">Data 01</text><text x="189" y="257">Data 02</text><text x="342" y="257">Data 03</text><text x="495" y="257">Data 04</text>
      </g>
      <polyline points="47,186 200,199 353,170 507,182" fill="none" stroke="var(--olive)" stroke-width="1.2"/>
      <polyline points="47,227 200,218 353,188 507,141" fill="none" stroke="var(--slate)" stroke-width="1.2"/>
      <g fill="var(--olive)"><circle cx="47" cy="186" r="1.8"/><circle cx="200" cy="199" r="1.8"/><circle cx="353" cy="170" r="1.8"/><circle cx="507" cy="182" r="1.8"/></g>
      <g fill="var(--slate)"><circle cx="47" cy="227" r="1.8"/><circle cx="200" cy="218" r="1.8"/><circle cx="353" cy="188" r="1.8"/><circle cx="507" cy="141" r="1.8"/></g>
    </svg>
    <p class="footer">Presented By Presenter | velora systems</p>
    <div class="page">6</div>
  </section>

  <!-- Bar slide -->
  <section class="slide bg-white">
    <div class="logo on-white"><span class="mark"></span>velora systems</div>
    <h2 class="headline" style="left:31px;top:41px">Bar Slide</h2>
    <div class="rule" style="left:31px;top:70px;width:145px"></div>
    <p class="lead" style="left:31px;top:84px;width:180px">Helps communicate data-driven insights in a visually compelling manner. Includes: Bar charts, pie charts, line graphs, and consistent formatting for clarity.</p>
    <div class="stat olive mini" style="left:32px;top:129px;width:92px;height:39px"><b style="font-size:16px">100</b><small>readers appreciate accurate information</small></div>
    <div class="stat slate mini" style="left:32px;top:175px;width:92px;height:39px"><b style="font-size:16px">75</b><small>readers appreciate accurate information</small></div>
    <div class="stat mist mini" style="left:32px;top:220px;width:92px;height:39px"><b style="font-size:16px">50</b><small>readers appreciate accurate information</small></div>
    <svg class="chart" width="549" height="309" viewBox="0 0 549 309" role="img" aria-label="Säulendiagramm mit drei Reihen für April bis Juli">
      <text x="160" y="195" font-size="6.5" fill="var(--ink)" transform="rotate(-90 160 195)">Werteachse</text>
      <g fill="var(--olive)"><rect x="187.5" y="237" width="19" height="31"/><rect x="272.5" y="221" width="19" height="47"/><rect x="359.5" y="171" width="19" height="97"/><rect x="444.5" y="93" width="19" height="175"/></g>
      <g fill="var(--slate)"><rect x="207.5" y="168" width="19" height="100"/><rect x="292.5" y="190" width="19" height="78"/><rect x="379.5" y="141" width="19" height="127"/><rect x="464.5" y="162" width="19" height="106"/></g>
      <g fill="var(--mist)"><rect x="227.5" y="177" width="19" height="91"/><rect x="312.5" y="199" width="19" height="69"/><rect x="399.5" y="235" width="19" height="33"/><rect x="484.5" y="195" width="19" height="73"/></g>
      <g font-size="6.5" font-weight="600" fill="var(--ink)" text-anchor="middle"><text x="217" y="279">April</text><text x="302" y="279">Mai</text><text x="389" y="279">Juni</text><text x="474" y="279">Juli</text></g>
    </svg>
    <p class="footer" style="top:280px">Presented By Presenter | velora systems</p>
    <div class="page" style="top:274px">7</div>
  </section>

  <!-- Pie slide -->
  <section class="slide bg-white">
    <div class="logo on-white"><span class="mark"></span>velora systems</div>
    <h2 class="headline" style="left:31px;top:113px">Pie Slide</h2>
    <div class="rule" style="left:31px;top:141px;width:145px"></div>
    <p class="lead" style="left:31px;top:157px;width:180px">Helps communicate data-driven insights in a visually compelling manner. Includes: Bar charts, pie charts, line graphs, and consistent formatting for clarity.</p>
    <svg class="chart" width="549" height="309" viewBox="0 0 549 309" role="img" aria-label="Ringdiagramm mit vier Anteilen">
      <g fill="none" stroke-width="18" transform="rotate(-90 316 113)">
        <circle cx="316" cy="113" r="66" stroke="var(--slate)" stroke-dasharray="113.7 414.7" stroke-dashoffset="0"/>
        <circle cx="316" cy="113" r="66" stroke="#b3af0a" stroke-dasharray="131 414.7" stroke-dashoffset="-115.2"/>
        <circle cx="316" cy="113" r="66" stroke="var(--bright)" stroke-dasharray="87.2 414.7" stroke-dashoffset="-247.7"/>
        <circle cx="316" cy="113" r="66" stroke="var(--mist)" stroke-dasharray="76.8 414.7" stroke-dashoffset="-336.4"/>
      </g>
    </svg>
    <div class="stat bright mini" style="left:110px;top:217px;width:92px;height:40px"><b style="font-size:16px">120</b><small>readers appreciate accurate information</small></div>
    <div class="stat olive mini" style="left:219px;top:217px;width:92px;height:40px"><b style="font-size:16px">100</b><small>readers appreciate accurate information</small></div>
    <div class="stat slate mini" style="left:325px;top:217px;width:93px;height:40px"><b style="font-size:16px">75</b><small>readers appreciate accurate information</small></div>
    <div class="stat mist mini" style="left:428px;top:217px;width:91px;height:40px"><b style="font-size:16px">50</b><small>readers appreciate accurate information</small></div>
    <p class="footer" style="top:280px">Presented By Presenter | velora systems</p>
    <div class="page" style="top:274px">8</div>
  </section>

  <!-- Table slide -->
  <section class="slide bg-olive">
    <div class="abs" style="left:0;top:0;width:206px;height:159px;background:var(--white)"></div>
    <div class="logo on-olive"><span class="mark"></span>velora systems</div>
    <h2 class="headline" style="left:31px;top:41px">Table Slide</h2>
    <div class="rule" style="left:31px;top:70px;width:145px"></div>
    <p class="lead" style="left:31px;top:84px;width:155px">Helps communicate data-driven insights in a visually compelling manner. Includes: Bar charts, pie charts, line graphs, and consistent formatting for clarity.</p>
    <span class="table-head" style="left:236px">Headline</span>
    <span class="table-head" style="left:307px">Headline</span>
    <span class="table-head" style="left:378px">Headline</span>
    <span class="table-head" style="left:449px">Headline</span>
    <svg class="chart" width="549" height="309" viewBox="0 0 549 309" aria-hidden="true">
      <g stroke="#e3e17a" stroke-width=".8">
        <line x1="236" y1="95" x2="520" y2="95"/><line x1="236" y1="135" x2="520" y2="135"/>
        <line x1="236" y1="177" x2="520" y2="177"/><line x1="236" y1="219" x2="520" y2="219"/>
        <line x1="307" y1="80" x2="307" y2="260"/><line x1="378" y1="80" x2="378" y2="260"/><line x1="449" y1="80" x2="449" y2="260"/>
      </g>
    </svg>
    <p class="footer">Presented By Presenter | velora systems</p>
    <div class="page light">9</div>
  </section>

  <!-- Comparison slide -->
  <section class="slide bg-white">
    <div class="logo on-white"><span class="mark"></span>velora systems</div>
    <h2 class="headline" style="left:26px;top:98px">Comparison</h2>
    <div class="rule" style="left:26px;top:127px;width:137px"></div>
    <p class="lead" style="left:280px;top:93px;width:220px;font-size:7.8px;color:var(--slate)">Highlights differences between options, concepts, or approaches in a structured format.<br><br>Includes: Two- or three-column layouts, equal or varied column widths, and clear labeling.</p>
    <div class="compare" style="left:25px">
      <div class="swatch"></div>
      <div class="body"><strong>Side 01</strong><br>Summarize the key points here.<ul><li>• Bullet points</li><li>• Bullet points</li></ul></div>
    </div>
    <div class="compare" style="left:280px">
      <div class="swatch"></div>
      <div class="body"><strong>Side 02</strong><br>Summarize the key points here.<ul><li>• Bullet points</li><li>• Bullet points</li></ul></div>
    </div>
    <p class="footer">Presented By Presenter | velora systems</p>
    <div class="page">10</div>
  </section>

  <!-- Timeline slide -->
  <section class="slide bg-white">
    <div class="logo on-white"><span class="mark"></span>velora systems</div>
    <h2 class="headline" style="left:31px;top:41px">Timeline Slide</h2>
    <div class="rule" style="left:31px;top:70px;width:145px"></div>
    <p class="lead" style="left:31px;top:84px;width:180px">Helps communicate data-driven insights in a visually compelling manner. Includes: Bar charts, pie charts, line graphs, and consistent formatting for clarity.</p>
    <div class="abs" style="left:31px;top:240px;width:476px;height:.8px;background:var(--grid)"></div>
    <span class="tl-label" style="left:18px;top:151px">Sign Off</span><div class="tl-dot" style="left:43px;top:157px;background:var(--olive-soft)"></div>
    <span class="tl-label" style="left:161px;top:151px">Assign PM</span><div class="tl-dot" style="left:186px;top:157px"></div>
    <span class="tl-label" style="left:253px;top:128px">Data Back-Up</span><div class="tl-dot" style="left:278px;top:134px"></div>
    <span class="tl-label" style="left:283px;top:172px">Checkpoint A</span><div class="tl-dot" style="left:308px;top:178px"></div>
    <span class="tl-label" style="left:154px;top:195px">Project Approval</span><div class="tl-dot" style="left:179px;top:201px"></div>
    <span class="tl-label" style="left:402px;top:195px">Certification</span><div class="tl-dot" style="left:427px;top:201px"></div>
    <span class="tl-label" style="left:461px;top:172px">Checkpoint B</span><div class="tl-dot" style="left:486px;top:178px"></div>
    <span class="tl-date" style="left:31px">01/19/25</span>
    <span class="tl-date" style="left:144px">04/12/25</span>
    <span class="tl-date" style="left:258px">07/05/25</span>
    <span class="tl-date" style="left:373px">09/27/25</span>
    <span class="tl-date" style="left:487px">12/20/25</span>
    <p class="footer" style="top:277px">Presented By Presenter | velora systems</p>
    <div class="page" style="top:271px">11</div>
  </section>

  <!-- Next steps slide -->
  <section class="slide bg-olive">
    <h2 class="headline" style="left:32px;top:41px">Next Steps</h2>
    <div class="rule" style="left:32px;top:69px;width:126px"></div>
    <p class="lead" style="left:32px;top:88px;width:130px;color:#eeec9a;font-size:6.4px">Where do you go from here? Sustainability reports are not just about looking back, but also looking forward. This SDG Progress Report is a continuous work in progress – a way for your organization to track its impact and improvements over time. This section outlines your strategy for continuing the good work done so far.</p>
    <div class="step-head" style="left:206px;top:32px">1. Step 01</div><div class="step-box" style="left:206px;top:53px">Outlines structured processes, workflows, or step-by-step guidance.</div>
    <div class="step-head" style="left:368px;top:32px">2. Step 02</div><div class="step-box" style="left:368px;top:53px">Outlines structured processes, workflows, or step-by-step guidance.</div>
    <div class="step-head" style="left:206px;top:116px">3. Step 03</div><div class="step-box" style="left:206px;top:138px">Outlines structured processes, workflows, or step-by-step guidance.</div>
    <div class="step-head" style="left:368px;top:116px">4. Step 04</div><div class="step-box" style="left:368px;top:138px">Outlines structured processes, workflows, or step-by-step guidance.</div>
    <div class="step-head" style="left:206px;top:201px">5. Step 05</div><div class="step-box" style="left:206px;top:222px">Outlines structured processes, workflows, or step-by-step guidance.</div>
    <div class="step-head" style="left:368px;top:201px">6. Step 06</div><div class="step-box" style="left:368px;top:222px">Outlines structured processes, workflows, or step-by-step guidance.</div>
    <p class="footer" style="top:277px;color:#eeec9a">Presented By Presenter | velora systems</p>
    <div class="page light" style="top:271px">12</div>
  </section>

  <!-- Conclusion slide -->
  <section class="slide bg-white">
    <h2 class="headline" style="left:31px;top:38px;font-size:11.5px;font-weight:600;line-height:1.4">Conclusion &amp; Next Steps Slide<br>(Closing &amp; Action Items)</h2>
    <div class="rule" style="left:31px;top:71px;width:144px"></div>
    <span class="close-step" style="top:74px">Step 01</span><span class="close-text" style="top:74px">next actions, contact details, or interactive Q&amp;A section.</span>
    <div class="close-rule" style="top:97px"></div>
    <span class="close-step" style="top:116px">Step 02</span><span class="close-text" style="top:116px">next actions, contact details, or interactive Q&amp;A section.</span>
    <div class="close-rule" style="top:139px"></div>
    <span class="close-step" style="top:159px">Step 03</span><span class="close-text" style="top:159px">next actions, contact details, or interactive Q&amp;A section.</span>
    <div class="close-rule" style="top:183px"></div>
    <span class="close-step" style="top:198px">Step 04</span><span class="close-text" style="top:198px">next actions, contact details, or interactive Q&amp;A section.</span>
    <div class="close-rule" style="top:222px"></div>
    <span class="close-step" style="top:239px">Step 05</span><span class="close-text" style="top:239px">next actions, contact details, or interactive Q&amp;A section.</span>
    <div class="page" style="top:271px">13</div>
  </section>

  <!-- Contact slide -->
  <section class="slide bg-olive">
    <div class="logo on-olive"><span class="mark"></span>velora systems</div>
    <h2 class="headline" style="left:59px;top:70px">Contact</h2>
    <div class="rule" style="left:59px;top:99px;width:91px"></div>
    <p class="lead" style="left:59px;top:114px;width:212px;color:var(--slate);font-size:6.6px">Guter Rat muss nicht teuer sein. Buche hier schnell, einfach und unverbindlich ein erstes Gespräch. Wir nehmen uns Zeit und sprechen über deine Möglichkeiten.</p>
    <p class="contact-line" style="top:168px;font-weight:500">Lindenweg 14<br>93047 Talheim in der Oberpfalz</p>
    <p class="contact-line" style="top:202px">+49 9400 7264018</p>
    <p class="contact-line" style="top:236px">www.velorasystems.example</p>
    <p class="contact-line" style="top:253px">post@velorasystems.example</p>
  </section>

</main>
</body>
</html>
```